Hopscotch Hattie needs updated Marketing Material!

Moving business to a new location and am looking to update all marketing material, including business cards, postcards, flyers, website. I've attached a copy of my current business card.
Updates

Good Morning!  I just received my new business phone number.  It is 724-305-9847

Hello All Designers!

Thank you for all the submissions I have received so far!  I wanted to give you a bit more background on what Hopscotch Hattie is all about:

I started this service when I was downsized out of a sales and marketing position.   A friend asked if I had time to run a few errands for her while she was at work.  "Lightbulb"!  I thought there must be more people that are over worked, over booked and want nothing more to do when they get home than spend time with their families or just relaxing.  And who wants to do all their running around on the weekends??  Hopscotch Hattie was born!

I have been extremely fortunate with my business here in California.  However, this summer I will be moving to a small town in Pennsylvania and I will be in uncharted territory.  I hope to have marketing material that will "WOW" all new potential clients.  Letting them know that I offer a unique service that can put time back into their week and free up their weekends for more important things.

If there is anything else I can tell you in order to help you with your design process, please let me know!
Thank you!
Hattie

Target Market(s)

Busy working parents and young professionals with disposable income that would like to spend their down time doing things that they enjoy rather than doing errands.

Industry/Entity Type

Marketing

```html
<!DOCTYPE html>
<html lang="en">
<head>
<meta charset="utf-8">
<title>Hopscotch Hattie – Business Card</title>
<link rel="stylesheet" href="https://fonts.googleapis.com/css2?family=Open+Sans:wght@300;400;700&display=swap">
<style>
  :root {
    --page-bg: #ecebef;
    --card-white: #ffffff;
    --brand-purple: #4f3f93;
    --brand-purple-light: #5e4fa8;
    --brand-purple-deep: #3f3180;
    --ink-dark: #2b2b2b;
    --ink-grey: #5a5a5a;
    --ink-light: #ffffff;
    --swoosh-black: #1c1c1c;
  }
  * { box-sizing: border-box; margin: 0; padding: 0; }
  html, body {
    width: 1200px; height: 800px; overflow: hidden;
    background: var(--page-bg);
    font-family: "Open Sans", Arial, sans-serif;
  }
  .sheet {
    width: 1200px; height: 800px;
    display: flex; align-items: center; justify-content: center; gap: 40px;
  }
  .card {
    position: relative;
    width: 540px; height: 309px;
    border-radius: 4px;
    overflow: hidden;
    box-shadow: 0 6px 18px rgba(30, 20, 60, 0.18);
  }

  /* Back of card */
  .card--back {
    background: linear-gradient(135deg, var(--brand-purple-light), var(--brand-purple-deep));
    color: var(--ink-light);
    display: flex; flex-direction: column; align-items: center; justify-content: center;
    text-align: center;
    padding: 24px;
  }
  .card--back .brand-name {
    font-weight: 300; font-size: 44px; line-height: 1; letter-spacing: -0.5px;
  }
  .card--back .brand-tagline {
    font-weight: 300; font-size: 17px; margin-top: 4px;
  }
  .service-list {
    list-style: none; margin-top: 18px;
    font-size: 13px; line-height: 1.45;
  }
  .card--back .motto {
    font-weight: 300; font-style: italic; font-size: 19px; margin-top: 20px;
  }

  /* Front of card */
  .card--front { background: var(--card-white); }
  .card-swoosh { position: absolute; inset: 0; }
  .wordmark {
    position: absolute; left: 110px; top: 30px;
    display: flex; align-items: center; gap: 14px;
  }
  .wordmark-dot {
    width: 58px; height: 58px; border-radius: 50%;
    background: var(--brand-purple);
    flex: none;
  }
  .wordmark-text .brand-name {
    font-weight: 300; font-size: 42px; line-height: 1; color: var(--ink-dark); letter-spacing: -0.5px;
  }
  .wordmark-text .brand-tagline {
    font-weight: 300; font-size: 15px; color: var(--ink-grey); margin-top: 2px;
  }
  .person {
    position: absolute; left: 120px; top: 112px;
  }
  .person-name {
    font-weight: 700; font-size: 20px; line-height: 1.3; color: var(--brand-purple); letter-spacing: 0.5px;
  }
  .person-role {
    font-size: 13px; color: var(--ink-dark); margin-left: 30px;
  }
  .contact-list {
    position: absolute; right: 22px; bottom: 16px;
    list-style: none; color: var(--ink-light);
    font-size: 14px; line-height: 1.45; text-align: right;
  }
  .contact-list li { display: flex; align-items: center; justify-content: flex-end; gap: 8px; }
  .contact-icon {
    width: 14px; height: 14px; border-radius: 2px;
    background: var(--ink-light);
    display: inline-flex; align-items: center; justify-content: center;
  }
</style>
</head>
<body>
<main class="sheet">

  <section class="card card--back" aria-label="Business card back">
    <h2 class="brand-name">Hopscotch Hattie</h2>
    <p class="brand-tagline">Personal Concierge and Errand Service</p>
    <ul class="service-list">
      <li>Personal Shopping and Errands</li>
      <li>Household Management</li>
      <li>Corporate Concierge</li>
      <li>Project Management</li>
      <li>Group Rates for Teachers and Seniors</li>
    </ul>
    <p class="motto">“We run around so you don’t have to!”</p>
  </section>

  <section class="card card--front" aria-label="Business card front">
    <svg class="card-swoosh" width="540" height="309" viewBox="0 0 540 309" aria-hidden="true">
      <path d="M0 165 C80 240 180 275 280 255 C380 235 470 195 540 160 L540 309 L0 309 Z" fill="var(--brand-purple)"/>
      <path d="M0 140 C80 222 180 262 280 244 C380 226 470 188 540 150 L540 160 C470 195 380 235 280 255 C180 275 80 240 0 165 Z" fill="var(--swoosh-black)"/>
    </svg>

    <div class="wordmark">
      <span class="wordmark-dot"></span>
      <div class="wordmark-text">
        <h1 class="brand-name">Hopscotch Hattie</h1>
        <p class="brand-tagline">Personal Concierge and Errand Service</p>
      </div>
    </div>

    <div class="person">
      <p class="person-name">HATTIE BRENNAN</p>
      <p class="person-role">Director</p>
    </div>

    <ul class="contact-list">
      <li>724-305-9847
        <span class="contact-icon"><svg width="10" height="10" viewBox="0 0 10 10" aria-hidden="true"><path d="M2 1 L4 1 L4.6 3 L3.4 4 C4 5.4 4.8 6.2 6 6.6 L7 5.4 L9 6 L9 8 C5 8.6 1.4 5 2 1 Z" fill="var(--brand-purple)"/></svg></span>
      </li>
      <li>hattie@hopscotchhattie.biz
        <span class="contact-icon"><svg width="10" height="10" viewBox="0 0 10 10" aria-hidden="true"><rect x="1" y="2.5" width="8" height="5.5" fill="none" stroke="var(--brand-purple)" stroke-width="1"/><path d="M1 2.5 L5 5.5 L9 2.5" fill="none" stroke="var(--brand-purple)" stroke-width="1"/></svg></span>
      </li>
      <li>www.hopscotchhattie.biz
        <span class="contact-icon"><svg width="10" height="10" viewBox="0 0 10 10" aria-hidden="true"><circle cx="5" cy="5" r="3.8" fill="none" stroke="var(--brand-purple)" stroke-width="1"/><path d="M1.2 5 H8.8 M5 1.2 C3 3.5 3 6.5 5 8.8 M5 1.2 C7 3.5 7 6.5 5 8.8" fill="none" stroke="var(--brand-purple)" stroke-width="0.8"/></svg></span>
      </li>
    </ul>
  </section>

</main>
</body>
</html>
```